M25 Billboard Advert Required Please

I need an advert for a motorway Billboard on the M25 , the advert should show the following in big letters:
GUTTER CLEANING
DALRYNFLUES.COM and a small logo off to the side (Our logo is attached)

The printer has requested the following (Important please) the advert has to be
pdf file / 300 dpi/landscape orientation / scaled to a minimum 25% advert size ( this particular site is 22ft x 10ft so 25% of this please). Please also make sure that the artwork is embedded and outlined correctly if this is incorrect it will affect the printing of the banner.

Target Market(s)

General Public

Industry/Entity Type

Gutter Cleaning

Requirements
Should not have
• No Change to our Logo

```html
<!DOCTYPE html>
<html lang="en">
<head>
<meta charset="utf-8">
<title>Gutter Cleaning – DalrynFlues.com</title>
<link rel="stylesheet" href="https://fonts.googleapis.com/css2?family=Rozha+One&family=Open+Sans:wght@700&display=swap">
<style>
  :root {
    --backdrop: #a7a8ac;
    --paper: #ffffff;
    --ink: #0d0d0d;
    --brand-red: #ab232b;
  }
  html, body {
    margin: 0;
    padding: 0;
    width: 1200px;
    height: 859px;
    overflow: hidden;
    background: var(--backdrop);
  }
  .billboard {
    position: absolute;
    left: 50px;
    top: 180px;
    width: 1100px;
    height: 500px;
    display: block;
  }
  .headline, .web-address {
    font-family: "Rozha One", Georgia, serif;
  }
  .headline { fill: var(--ink); font-size: 195px; }
  .web-address { fill: var(--paper); font-size: 142px; }
  .brand-name, .brand-tagline {
    font-family: "Open Sans", Arial, sans-serif;
    font-weight: 700;
    fill: var(--paper);
  }
  .brand-name { font-size: 27px; }
  .brand-tagline { font-size: 12.5px; }
  .band-top { fill: var(--paper); }
  .band-bottom { fill: var(--brand-red); }
  .web-badge { fill: var(--paper); }
  .web-globe { fill: none; stroke: var(--brand-red); stroke-width: 2.6; }
</style>
</head>
<body>
<svg class="billboard" viewBox="0 0 1100 500" xmlns="http://www.w3.org/2000/svg" role="img" aria-label="Gutter Cleaning billboard for DalrynFlues.com">
  <rect class="band-top" x="0" y="0" width="1100" height="277"/>
  <rect class="band-bottom" x="0" y="277" width="1100" height="223"/>

  <text class="headline" x="70" y="222" textLength="960" lengthAdjust="spacingAndGlyphs">Gutter Cleaning</text>

  <g class="web-icon" transform="translate(531 281)">
    <circle class="web-badge" r="31"/>
    <circle class="web-globe" r="22"/>
    <ellipse class="web-globe" rx="10" ry="22"/>
    <line class="web-globe" x1="0" y1="-22" x2="0" y2="22"/>
    <line class="web-globe" x1="-22" y1="0" x2="22" y2="0"/>
    <line class="web-globe" x1="-19" y1="-11" x2="19" y2="-11"/>
    <line class="web-globe" x1="-19" y1="11" x2="19" y2="11"/>
  </g>

  <text class="web-address" x="78" y="426" textLength="705" lengthAdjust="spacingAndGlyphs">DalrynFlues.com</text>

  <g class="brand-lockup">
    <text class="brand-name" x="1021" y="400" text-anchor="end">Dalryn Flues</text>
    <text class="brand-tagline" x="810" y="423" textLength="211" lengthAdjust="spacingAndGlyphs">Clean gutters protect your property</text>
  </g>
</svg>
</body>
</html>
```